Book cover design for the book titled "Quieter Under Lanterns."

create a book cover. The book title is, "Quieter Under Lanterns: A Ledger of Harbour Songs Across Mild Winters." The purpose of the book is to create awareness of how childhood trauma is impacting 7 out of 10 adults in the world today and that two-thirds of children will experience neglect and or abuse before their 18th birthday. One victim described that his mental and physical illness resulting from childhood trauma felt like he wa being pulled to the ground, that the force was "quieter under lanterns." The design should be clean and simple and communicate a crisis.

```html
<!DOCTYPE html>
<html lang="en">
<head>
<meta charset="UTF-8">
<title>Quieter Under Lanterns — Book Cover</title>
<link rel="stylesheet" href="https://fonts.googleapis.com/css2?family=Russo+One&family=Saira+Condensed:wght@500&family=Archivo:wght@500&display=swap">
<style>
  :root {
    --page-bg: #f2f2f2;
    --cover-black: #0b0b0b;
    --photo-light: #8a8a8a;
    --photo-mid: #3a3a3a;
    --photo-dark: #121212;
    --type-white: #f5f5f5;
  }
  * { box-sizing: border-box; margin: 0; padding: 0; }
  html, body {
    width: 1200px;
    height: 864px;
    overflow: hidden;
    background: var(--page-bg);
  }
  .stage {
    width: 1200px;
    height: 864px;
    display: flex;
    align-items: center;
    justify-content: center;
  }
  .book-cover {
    position: relative;
    width: 570px;
    height: 820px;
    background: var(--cover-black);
    overflow: hidden;
  }
  .cover-photo {
    position: absolute;
    left: 0;
    top: 0;
    width: 100%;
    height: 76%;
    background:
      linear-gradient(180deg, rgba(11,11,11,0) 70%, var(--cover-black) 100%),
      linear-gradient(100deg, var(--photo-light) 0%, var(--photo-mid) 22%, var(--photo-dark) 40%, #1c1c1c 55%, #5a5a5a 68%, #1a1a1a 82%, var(--photo-dark) 100%);
  }
  .title-block {
    position: absolute;
    right: 34px;
    bottom: 70px;
    text-align: right;
    color: var(--type-white);
  }
  .title-line-one {
    font-family: "Saira Condensed", sans-serif;
    font-weight: 500;
    font-size: 74px;
    line-height: 0.9;
    letter-spacing: 2px;
    margin-right: 150px;
  }
  .title-line-two {
    font-family: "Archivo", sans-serif;
    font-weight: 500;
    font-size: 24px;
    letter-spacing: 8px;
    line-height: 1;
    margin-right: 190px;
    margin-top: 2px;
  }
  .title-line-three {
    font-family: "Russo One", sans-serif;
    font-size: 96px;
    line-height: 0.95;
    letter-spacing: 1px;
  }
  .subtitle {
    font-family: Arial, Helvetica, sans-serif;
    font-size: 15px;
    line-height: 1.2;
    margin-top: 10px;
    color: var(--type-white);
  }
</style>
</head>
<body>
  <main class="stage">
    <section class="book-cover">
      <div class="cover-photo" role="img" aria-label="Black and white photograph of a small child half hidden behind a doorway, lit by a narrow shaft of light"></div>
      <div class="title-block">
        <h1>
          <span class="title-line-one" style="display:block">QUIETER</span>
          <span class="title-line-two" style="display:block">UNDER</span>
          <span class="title-line-three" style="display:block">Lanterns</span>
        </h1>
        <p class="subtitle">A Ledger of Harbour Songs Across Mild Winters</p>
      </div>
    </section>
  </main>
</body>
</html>
```